Style Template created - Report Accounting and Advisory industry

We need a style template created to set out a report for advice. The report follows <br/><br/>- Cover Page - ( we would need to print to a letter head )<br/>- General Disclaimer<br/>- Space to add Excel Reports in to the document- Maybe inserted Pdf's later<br/>- Action Plan dot points under headings<br/>- List of Strategies to be adopted<br/><br/>Attached is a quick example word doc that needs Custom Style Templates made so that we can quickly format items added. Also the ugly PDF that we currently produce for clients <br/><br/>Red - is our preferred Colour<br/><br/>

Target Market(s)

Accounting / Business / Professionals

Industry/Entity Type

Accounting

Colors
ec1f27

Requirements
Nice to have
• Simple Clean design. Not to busy. Easy to modify the "wording text" in design
Should not have
• Too busy or too much color

```html
<!DOCTYPE html>
<html lang="en">
<head>
<meta charset="utf-8">
<title>Hartwell Reid – Report Letterhead</title>
<link href="https://fonts.googleapis.com/css2?family=Source+Sans+3:wght@400;600&display=swap" rel="stylesheet">
<style>
  :root {
    --brand-red: #ec1f27;
    --heading-red: #e10a14;
    --text-grey: #6d6e71;
    --rule-grey: #c7c8ca;
    --panel-grey: #e6e7e8;
    --page: #ffffff;
  }
  * { margin: 0; padding: 0; box-sizing: border-box; }
  html, body { width: 856px; height: 1200px; overflow: hidden; background: var(--page); }
  body { font-family: "Source Sans 3", sans-serif; color: var(--text-grey); }
  .page { position: relative; width: 856px; height: 1200px; background: var(--page); }

  .brand { position: absolute; left: 91px; top: 40px; }
  .brand-name {
    font-size: 29px; font-weight: 600; color: var(--brand-red);
    letter-spacing: 0.5px; line-height: 1; text-transform: uppercase;
  }
  .brand-tagline {
    margin-top: 4px; font-size: 9px; letter-spacing: 0.3px;
    color: var(--text-grey); text-transform: uppercase;
  }
  .brand-mark { position: absolute; left: 699px; top: 33px; }

  .section { position: absolute; left: 85px; width: 690px; }
  .section-heading {
    font-size: 21px; font-weight: 400; color: var(--heading-red);
    letter-spacing: 3px; line-height: 26px; text-transform: uppercase;
    margin-bottom: 6px;
  }
  .body-copy { font-size: 13.2px; line-height: 27.8px; letter-spacing: 0.15px; }

  .callout {
    position: absolute; left: 81px; top: 932px; width: 468px; height: 66px;
    background: var(--panel-grey); border-radius: 5px;
  }
  .callout-text {
    position: absolute; left: 85px; top: 954px; width: 690px;
    font-size: 13.2px; line-height: 27.8px; letter-spacing: 0.15px;
    transform: translateY(-14px);
  }
  .subline {
    position: absolute; left: 84px; top: 1003px;
    font-size: 16px; letter-spacing: 0.4px;
  }

  .contact-bar { position: absolute; top: 1104px; left: 0; width: 856px; }
  .contact-item {
    position: absolute; font-size: 11px; line-height: 16px; color: var(--text-grey);
  }
  .contact-divider {
    position: absolute; top: -1px; width: 1px; height: 31px; background: var(--rule-grey);
  }
  .footer-band {
    position: absolute; left: 0; bottom: 0; width: 856px; height: 25px;
    background: var(--heading-red);
  }
</style>
</head>
<body>
<div class="page">
  <header class="brand">
    <div class="brand-name">Hartwell Reid</div>
    <div class="brand-tagline">Chartered Accountants</div>
  </header>
  <svg class="brand-mark" width="44" height="44" viewBox="0 0 44 44" aria-hidden="true">
    <circle cx="22" cy="22" r="21" fill="var(--brand-red)"/>
  </svg>

  <section class="section" style="top:152px; left:82px;">
    <h2 class="section-heading">Lorem ipsum dolor sit amet</h2>
    <p class="body-copy">Lorem ipsum dolor sit amet, consectetur adipisicing elit, sed do eiusmod tempor incididunt ut labore et dolore magna aliqua. Ut enim ad minim veniam, quis nostrud exercitation ullamco laboris nisi ut aliquip ex ea commodo consequat. Duis aute irure dolor in reprehenderit in voluptate velit esse cillum dolore eu fugiat nulla pariatur. Excepteur sint occaecat cupidatat non proident, sunt in culpa qui officia deserunt mollit anim id est laborum.</p>
  </section>

  <section class="section" style="top:343px;">
    <h2 class="section-heading">Lorem ipsum dolor sit amet</h2>
    <p class="body-copy">Lorem ipsum dolor sit amet, consectetur adipisicing elit, sed do eiusmod tempor incididunt ut labore et dolore magna aliqua. Ut enim ad minim veniam, quis nostrud exercitation ullamco laboris nisi ut aliquip ex ea commodo consequat. Duis aute irure dolor in reprehenderit in voluptate velit esse cillum dolore eu fugiat nulla pariatur. Excepteur sint occaecat cupidatat non proident, sunt in culpa qui officia deserunt mollit anim id est laborum.</p>
  </section>

  <section class="section" style="top:538px;">
    <h2 class="section-heading">Lorem ipsum dolor sit amet</h2>
    <p class="body-copy">Lorem ipsum dolor sit amet, consectetur adipisicing elit, sed do eiusmod tempor incididunt ut labore et dolore magna aliqua. Ut enim ad minim veniam, quis nostrud exercitation ullamco laboris nisi ut aliquip ex ea commodo consequat. Duis aute irure dolor in reprehenderit in voluptate velit esse cillum dolore eu fugiat nulla pariatur. Excepteur sint occaecat cupidatat non proident, sunt in culpa qui officia deserunt mollit anim id est laborum.</p>
  </section>

  <section class="section" style="top:715px;">
    <p class="body-copy">Sed ut perspiciatis unde omnis iste natus error sit voluptatem accusantium doloremque laudantium, totam rem aperiam, eaque ipsa quae ab illo inventore veritatis et quasi architecto beatae vitae dicta sunt explicabo. Nemo enim ipsam voluptatem quia voluptas sit aspernatur aut odit aut fugit, sed quia consequuntur magni dolores eos qui ratione voluptatem sequi nesciunt. Neque porro quisquam est, qui dolorem ipsum quia dolor sit amet, consectetur, adipisci velit, sed quia non numquam eius modi tempora incidunt ut labore et dolore magnam aliquam quaerat voluptatem. Ut enim ad minima veniam, quis nostrum exercitationem ullam corporis suscipit laboriosam, nisi ut aliquid ex ea commodi consequatur.</p>
  </section>

  <div class="callout"></div>
  <p class="callout-text">Quis autem vel eum iure reprehenderit qui in ea voluptate velit esse quam nihil molestiae consequatur, vel illum qui dolorem eum fugiat quo voluptas nulla pariatur</p>
  <p class="subline">Sed ut perspiciatis unde omnis iste natus</p>

  <footer class="contact-bar">
    <div class="contact-item" style="left:94px;">Lorem Ipsm<br>Lorem Ipsm dolor</div>
    <span class="contact-divider" style="left:214px;"></span>
    <div class="contact-item" style="left:248px;">Tel.: + 00 000 000 00<br>Lorem Ipsm dolor@Lorem Ipsum</div>
    <span class="contact-divider" style="left:441px;"></span>
    <div class="contact-item" style="left:480px;">123 Lorem Ipsm<br>Lorem Ipsm dolor</div>
    <span class="contact-divider" style="left:617px;"></span>
    <div class="contact-item" style="left:655px;">Lorem Ipsm<br>Lorem Ipsm dolor</div>
  </footer>

  <div class="footer-band"></div>
</div>
</body>
</html>
```